Motor Vault Website - Part of the Brantley Group

A complimentary website is required for the launch of a 'Motor Vault' - a new service launched by industry renowned BRANTLEY. Motor Vault is an industry-first brand that designs and builds unique subterranean car parks for private residential homes in London and the influential counties within the UK. Please see here the direction of a new BRANTLEY Website - we would like Motor Vault to be complimentary and sit alongside BRANTLEY harmoniously - https://www.brantleyhomes.example/brantley-nu-staging Brantley have some images, but whilst more professional images are in production - we have also attached pixmora photos- named clearly as pixmora. **Attached files include JPEG, .eps of logo and Brantley library images and Pixmora Library Images - two versions of logo dependent on background colour. - Website needs to be sleek, chic and masculine.- Colour Palette - Grey/ Black/ White - Same visiual journey as Brantley website- Required areas within the sit include - About Us / Our Work / Contact Page

Target Market(s)

Luxury
Men

Number of Pages Required

2 page

Font styles to use
Sans Serif

Colors
e8e8e8
757575
1b1b1b
000000
9d9d9d
cbcbcb
f5f5f5

Requirements
Must have
• Complimentary of this site - https://www.brantleyhomes.example/brantley-nu-staging
Should not have
• Colour

```html
<!DOCTYPE html>
<html lang="en">
<head>
<meta charset="utf-8">
<title>Motor Vault – Part of the Brantley Group</title>
<link rel="stylesheet" href="https://fonts.googleapis.com/css2?family=Oswald:wght@400;500&family=Raleway:wght@400;700;800&display=swap">
<style>
:root{
  --black:#000000;
  --ink:#1b1b1b;
  --nav:#221f20;
  --grey-dark:#757575;
  --grey-mid:#9d9d9d;
  --grey-light:#cbcbcb;
  --grey-pale:#e8e8e8;
  --white-soft:#f5f5f5;
  --white:#ffffff;
  --accent:#fff200;
}
*{box-sizing:border-box;margin:0;padding:0}
html,body{width:1200px;height:2356px;overflow:hidden}
body{position:relative;background:var(--white);font-family:'Oswald',sans-serif;color:var(--ink)}
.abs{position:absolute}

/* top bar & nav */
.topbar{left:0;top:0;width:1200px;height:20px;background:var(--black);color:var(--white);font-size:9px;letter-spacing:.3px}
.topbar .address{position:absolute;left:248px;top:4px}
.topbar .phone{position:absolute;right:250px;top:4px}
.site-nav{left:0;top:20px;width:1200px;height:55px;background:var(--nav)}
.brand{position:absolute;display:flex;align-items:center;gap:6px;color:var(--white)}
.brand .mark{width:16px;height:16px;background:var(--white)}
.brand .name{font-family:'Raleway',sans-serif;font-weight:700;font-size:24px;letter-spacing:1px}
.brand .tag{position:absolute;left:22px;top:27px;font-size:6px;letter-spacing:.6px;color:var(--grey-light);font-family:'Oswald',sans-serif;white-space:nowrap}
.site-nav .brand{left:248px;top:12px}
.menu a{position:absolute;top:19px;color:var(--white);text-decoration:none;font-size:13px}

/* hero */
.hero{left:0;top:75px;width:1200px;height:398px;background:radial-gradient(ellipse at 65% 40%,#4a4a4a 0%,#262626 45%,#0e0e0e 100%)}
.hero h1{position:absolute;left:248px;top:142px;font-family:'Raleway',sans-serif;font-weight:400;font-size:34px;color:var(--white)}
.hero h1 strong{color:var(--accent);font-weight:700}
.hero p{position:absolute;left:248px;top:186px;font-family:'Raleway',sans-serif;font-size:23px;color:var(--white)}
.btn{position:absolute;background:var(--accent);color:var(--ink);font-size:10px;text-align:center;text-decoration:none}
.hero .btn{left:248px;top:230px;width:100px;height:20px;line-height:20px}

/* section titles */
.section-title{position:absolute;left:0;width:1200px;text-align:center;font-family:'Raleway',sans-serif;font-weight:800;font-size:25px}
.section-title::after{content:"";display:block;margin:4px auto 0;width:140px;height:1px;background:currentColor;opacity:.5}

/* our work */
.our-work{left:0;top:473px;width:1200px;height:360px;background:linear-gradient(180deg,var(--white) 0%,var(--white-soft) 50%,var(--grey-pale) 100%);overflow:hidden}
.our-work .ghost{position:absolute;left:-30px;top:-10px;font-family:'Raleway',sans-serif;font-weight:700;font-size:190px;letter-spacing:14px;color:rgba(0,0,0,.06);white-space:nowrap}
.our-work .section-title{top:50px}
.work-item{position:absolute;width:220px;text-align:center;font-size:12.5px;color:var(--ink)}
.work-item .photo{width:157px;height:157px;margin:0 auto 20px;border-radius:50%;background:radial-gradient(circle at 50% 45%,#8a8a8a 0%,#3a3a3a 55%,#111 100%);position:relative}
.work-item .btn{left:28px;top:65px;width:100px;height:27px;line-height:27px}

/* about */
.about{left:0;top:833px;width:1200px;height:440px;background:linear-gradient(180deg,#0d0d0d 0%,#2a2a2a 60%,#161616 100%)}
.about .section-title{top:50px;color:var(--white)}
.about .frame{position:absolute;left:537px;top:139px;width:362px;height:239px;border:2px solid var(--grey-light);padding:6px}
.about .frame .photo{width:100%;height:100%;background:radial-gradient(ellipse at 50% 60%,#cfcfcf 0%,#6a6a6a 40%,#222 100%)}
.about .copy{position:absolute;left:295px;top:157px;width:305px;height:204px;background:var(--white);padding:12px 17px;font-size:10.2px;line-height:17px;color:var(--ink)}
.about .copy em{font-style:normal;color:var(--grey-mid)}

/* accreditations */
.accreditations{left:0;top:1273px;width:1200px;height:188px;background:var(--grey-pale)}
.badge{position:absolute;top:59px;width:143px;height:77px;background:var(--white-soft)}
.badge span{position:absolute;left:46px;top:14px;width:50px;height:50px;border-radius:50%;background:var(--grey-light)}

/* news */
.news{left:0;top:1461px;width:1200px;height:440px;background:linear-gradient(180deg,var(--white) 0%,var(--white-soft) 100%)}
.news .section-title{top:54px}
.news .card{position:absolute;left:610px;top:157px;width:308px;height:204px;background:var(--black);color:var(--white);text-align:right;padding:20px 12px 0 40px}
.news .card h3{font-weight:400;font-size:10.5px;line-height:14px}
.news .card p{margin-top:20px;font-size:10.5px;line-height:14px;padding-left:30px}
.news .card .btn{right:12px;top:162px;width:100px;height:23px;line-height:23px;font-size:10px}
.news .photo{position:absolute;left:284px;top:141px;width:359px;height:238px;background:radial-gradient(ellipse at 45% 30%,#d8d8d8 0%,#555 35%,#1a1a1a 100%)}

/* contact */
.contact{left:0;top:1901px;width:1200px;height:455px;background:linear-gradient(180deg,#1c1c1c 0%,#3a3a3a 55%,#1a1a1a 100%);color:var(--white)}
.contact .section-title{top:46px;color:var(--white)}
.contact .brand{left:248px;top:122px}
.details{position:absolute;left:250px;font-size:10px;line-height:13px}
.details::after{content:"";display:block;width:90px;height:1px;background:var(--grey-mid);margin-top:8px}
.socials{position:absolute;left:250px;top:292px;display:flex;gap:12px}
.socials span{width:14px;height:14px;background:var(--grey-mid)}
.field{position:absolute;left:679px;width:271px;height:24px}
.field svg{position:absolute;left:0;top:6px}
.field label{position:absolute;left:22px;top:5px;font-size:9.5px;color:var(--grey-light)}
.field .box{position:absolute;left:58px;top:0;width:213px;height:24px;border:2px solid var(--white)}
.form-note{position:absolute;left:679px;font-size:9px;color:var(--grey-light)}
.textarea{position:absolute;left:679px;top:248px;width:271px;height:65px;border:2px solid var(--white)}
.contact .btn{left:869px;top:327px;width:81px;height:22px;line-height:22px}
.legal{position:absolute;top:437px;font-size:7.5px;color:var(--white)}
</style>
</head>
<body>

<header>
  <div class="abs topbar">
    <span class="address">48 HARROW YARD, LONDON, W2 5QT</span>
    <span class="phone">TEL: 0207 555 0192</span>
  </div>
  <nav class="abs site-nav">
    <div class="brand"><span class="mark"></span><span class="name">MOTOR VAULT</span><span class="tag">PART OF THE BRANTLEY GROUP</span></div>
    <div class="menu">
      <a href="#" style="left:676px">Home</a>
      <a href="#" style="left:740px">About Us</a>
      <a href="#" style="left:826px">Our Work</a>
      <a href="#" style="left:913px">Contact</a>
    </div>
  </nav>
</header>

<section class="abs hero" role="img" aria-label="Black and white overhead photo of a worker in a hard hat among timber and steel on a construction site">
  <h1>Welcome to <strong>MOTOR VAULT</strong></h1>
  <p>London's Most Experienced</p>
  <a class="btn" href="#">Contact Us</a>
</section>

<section class="abs our-work">
  <div class="ghost" aria-hidden="true">MOTOR VAULT</div>
  <h2 class="section-title">OUR WORK</h2>
  <div class="work-item" style="left:215px;top:114px">
    <div class="photo" role="img" aria-label="Underground car park interior with a lit garage door"></div>
    CAR PARKINGS
  </div>
  <div class="work-item" style="left:490px;top:114px">
    <div class="photo" role="img" aria-label="Temporary works and demolition site"><a class="btn" href="#">VIEW MORE</a></div>
    <span style="position:relative;top:3px">TEMPORARY WORKS &amp; DEMOLITION</span>
  </div>
  <div class="work-item" style="left:763px;top:114px">
    <div class="photo" role="img" aria-label="Concrete basement under construction with columns"></div>
    <span style="position:relative;top:3px">BASEMENT CONSTRUCTION</span>
  </div>
</section>

<section class="abs about" role="img" aria-label="Dark London city skyline at night">
  <h2 class="section-title">ABOUT US</h2>
  <div class="frame"><div class="photo" role="img" aria-label="Finished concrete basement car park with columns"></div></div>
  <div class="copy">
    Today, <em>Motor Vault</em> designs and builds hundreds of <em>Unique Subterranean Car Parks</em> for private residential homes in London and the influential counties within the UK.<br>
    With an exceptional track record for delivering projects on time and in budget, Motor Vault offers the best value in this highly specialised field. Motor Vault operates a dependable, financially strong and leading London construction business which has been awarded <em>AUCB plus membership</em>. Motor Vault is the trusted partner for some of <em>London's most noteworthy architects and property developers.</em>
  </div>
</section>

<section class="abs accreditations" aria-label="Accreditations">
  <svg class="abs" style="left:250px;top:84px" width="14" height="28" viewBox="0 0 14 28"><path d="M12 1 2 14l10 13" fill="none" stroke="#757575" stroke-width="1.5"/></svg>
  <div class="badge" style="left:286px"><span></span></div>
  <div class="badge" style="left:448px"><span></span></div>
  <div class="badge" style="left:610px"><span></span></div>
  <div class="badge" style="left:771px"><span></span></div>
  <svg class="abs" style="left:935px;top:84px" width="14" height="28" viewBox="0 0 14 28"><path d="M2 1l10 13L2 27" fill="none" stroke="#000" stroke-width="1.5"/></svg>
</section>

<section class="abs news">
  <h2 class="section-title">LATEST NEWS</h2>
  <article class="card">
    <h3>TYPICAL TIMELINES FOR LONDON BASEMENT CONSTRUCTION PROJECTS.</h3>
    <p>The most common question from Motor Vault basement clients in London is 'how long will it take?'. There is no simple answer as each basement conversion project is unique. Whether you're an architect designing a basement for a client or you're contemplating a basement...</p>
    <a class="btn" href="#">Read More</a>
  </article>
  <div class="photo" role="img" aria-label="Worker in a dim basement site lit by a shaft of light"></div>
</section>

<footer class="abs contact" role="img" aria-label="Dark blurred photo of building services and cables">
  <h2 class="section-title">CONTACT US</h2>
  <div class="brand"><span class="mark"></span><span class="name">MOTOR VAULT</span><span class="tag">PART OF THE BRANTLEY GROUP</span></div>
  <div class="details" style="top:170px">Located In 48 HARROW YARD,<br>LONDON, W2 5QT</div>
  <div class="details" style="top:218px">Email: INFO@BRANTLEYHOMES.EXAMPLE</div>
  <div class="details" style="top:255px">Tel: 0207 555 0192</div>
  <div class="socials" aria-label="Social links"><span></span><span></span><span></span><span></span></div>

  <div class="field" style="top:126px">
    <svg width="12" height="12" viewBox="0 0 12 12"><circle cx="6" cy="3.5" r="3" fill="#fff"/><path d="M0 12c0-4 3-5.5 6-5.5s6 1.5 6 5.5z" fill="#fff"/></svg>
    <label>Name</label><div class="box"></div>
  </div>
  <div class="field" style="top:162px">
    <svg width="12" height="12" viewBox="0 0 12 12"><rect x="0" y="2" width="12" height="8" fill="#fff"/><path d="M0 2l6 4 6-4" fill="none" stroke="#333" stroke-width="1"/></svg>
    <label>Email</label><div class="box"></div>
  </div>
  <div class="field" style="top:198px">
    <svg width="12" height="12" viewBox="0 0 12 12"><path d="M2 1l2.5 0 1 3-1.5 1a7 7 0 0 0 3 3l1-1.5 3 1V11a1 1 0 0 1-1 1A10 10 0 0 1 1 2a1 1 0 0 1 1-1z" fill="#fff"/></svg>
    <label>Phone</label><div class="box"></div>
  </div>
  <div class="form-note" style="top:231px">Describe Your Project In a Few Sentences</div>
  <div class="textarea"></div>
  <div class="form-note" style="top:330px">We will contact you within one business day.</div>
  <a class="btn" href="#">Submit</a>

  <div class="legal" style="left:248px">COPYRIGHT © MOTOR VAULT 2019. TERMS AND CONDITIONS | PRIVACY POLICY</div>
  <div class="legal" style="right:250px">Designed &amp; Developed By NORTHGATE STUDIO</div>
</footer>

</body>
</html>
```